Q-Rolls Business Card

We are a modern retail clothing store. Established in 1994. I need a presentable card that will amaze vendors when given to them.

Front: Logo in middle
Info Side:

Name: Tomas Velder
Cell: 630-812-4463
Work: 630-917-3384 EXT. 417
Email: Tomas@q-rolls-example.com
Website: www.Q-rolls-example.com

Industry/Entity Type

Business

```html
<!DOCTYPE html>
<html lang="en">
<head>
<meta charset="utf-8">
<title>Q-Rolls Business Card</title>
<link href="https://fonts.googleapis.com/css2?family=Open+Sans:wght@400;600;700&display=swap" rel="stylesheet">
<style>
  :root {
    --backdrop-top: #ababab;
    --backdrop-bottom: #929292;
    --card-light: #ffffff;
    --card-dark: #000000;
    --ink: #111111;
    --ink-soft: #444444;
    --paper-text: #ffffff;
  }
  * { margin: 0; padding: 0; box-sizing: border-box; }
  html, body {
    width: 1200px;
    height: 900px;
    overflow: hidden;
  }
  body {
    position: relative;
    background: linear-gradient(to bottom, var(--backdrop-top), var(--backdrop-bottom));
    font-family: "Open Sans", Arial, sans-serif;
  }
  .card {
    position: absolute;
    top: 306px;
    width: 440px;
    height: 271px;
    border-radius: 10px;
    box-shadow: 0 1px 3px rgba(0,0,0,0.18);
  }
  .card--info { left: 149px; background: var(--card-light); }
  .card--front { left: 608px; background: var(--card-dark); }

  .wordmark {
    position: absolute;
    font-weight: 700;
    letter-spacing: 0.5px;
    line-height: 1;
    white-space: nowrap;
  }
  .card--info .wordmark {
    left: 70px;
    top: 118px;
    font-size: 34px;
    color: var(--ink);
  }
  .card--front .wordmark {
    left: 50%;
    top: 50%;
    transform: translate(-50%, -50%);
    font-size: 50px;
    color: var(--paper-text);
  }

  .contact {
    position: absolute;
    left: 239px;
    top: 80px;
  }
  .contact__name {
    font-size: 16px;
    font-weight: 600;
    color: var(--ink);
    margin-bottom: 17px;
  }
  .contact__list { list-style: none; }
  .contact__item {
    display: flex;
    align-items: center;
    font-size: 12.5px;
    color: var(--ink-soft);
    height: 18.2px;
    white-space: nowrap;
  }
  .contact__icon {
    width: 9px;
    height: 9px;
    margin-right: 9px;
    flex: none;
    fill: var(--ink);
  }
</style>
</head>
<body>
  <section class="card card--info" aria-label="Info side">
    <div class="wordmark">Q-Rolls</div>
    <div class="contact">
      <p class="contact__name">Tomas Velder</p>
      <ul class="contact__list">
        <li class="contact__item">
          <svg class="contact__icon" viewBox="0 0 10 10" aria-hidden="true"><path d="M2.5 0h5a1 1 0 0 1 1 1v8a1 1 0 0 1-1 1h-5a1 1 0 0 1-1-1V1a1 1 0 0 1 1-1zm0.6 1.2v6.6h3.8V1.2z"/></svg>
          630-812-4463
        </li>
        <li class="contact__item">
          <svg class="contact__icon" viewBox="0 0 10 10" aria-hidden="true"><path d="M2 0.3l1.6 2.1-0.9 1.2c0.6 1.3 1.5 2.2 2.8 2.8l1.2-0.9 2.1 1.6-0.9 2.3C4 9.2 0.8 6 0.3 1.4z"/></svg>
          630-917-3384 EXT. 417
        </li>
        <li class="contact__item">
          <svg class="contact__icon" viewBox="0 0 10 10" aria-hidden="true"><path d="M0 1.5h10v7H0zM0.8 2.3L5 5.5l4.2-3.2z" fill-rule="evenodd"/></svg>
          Tomas@q-rolls-example.com
        </li>
        <li class="contact__item">
          <svg class="contact__icon" viewBox="0 0 10 10" aria-hidden="true"><circle cx="5" cy="5" r="5"/><path d="M2 3.5c1 0 1.5 0.8 1.2 1.6-0.3 0.7 0.4 1.4 0.4 2.4M6 1c0 1 1 1 1.6 1.6M7 6.5c0.6 0.3 1 1 0.8 1.8" stroke="#fff" stroke-width="0.8" fill="none"/></svg>
          www.Q-rolls-example.com
        </li>
      </ul>
    </div>
  </section>

  <section class="card card--front" aria-label="Front side">
    <div class="wordmark">Q-Rolls</div>
  </section>
</body>
</html>
```